Coravelle barber salon has created a lotion and needs help titling.Plume by coravelle ?Corav

The product is for a lotion bottle , my prototype lotion bottle size is an 8oz black lotion bottle with pump. I want the label in florescent green. It should tap into the emotion of potential buyers. The design should say choose me 😀(not literally ). Though the text should be clear and punchy . I.e " the skin multi-vitamin." I'm looking for a designer intrigued by the thought of my lotion. The label should be georgeous,informative, with visuals that immediately convey what my product is and how it works.Not distracting, but clear and punchy, with no expectation of someone to read more than a couple of words.The text should support the visual in a way the visual could not. It seems that nowadays visuals are taking over with very little text. The font,color , or punch of color should be enticing.
So here are some particular ideas of points about the lotion that could possibly be put on back as is done by lotion makers.
.ingredients
.QRB approved
.portion of proceeds go to lift the meadows
.TC circled ( which is for pending trademark)
. I would like the word New in fluorescent on the bottle
.P.O Box address of place of manufacturing product.
. To help skin stay slightly moist,soft,and flexible with a smooth fine grained texture.

Target Market(s)

its a lotion so I want it available for all

Industry/Entity Type

Barber

Colors
9bcb3c

Requirements
Must have
• the word" Plume" and By coravelle...the word new on the bottle visible

```html
<!DOCTYPE html>
<html lang="en">
<head>
<meta charset="utf-8">
<title>Plume by Coravelle – Lotion Label</title>
<link rel="stylesheet" href="https://fonts.googleapis.com/css2?family=Questrial&family=Open+Sans:wght@400;700;800&display=swap">
<style>
  :root {
    --page-bg: #e6e6e6;
    --label-black: #1e1e1e;
    --brand-green: #9bcb3c;
    --wave-light: #a9d64e;
    --wave-deep: #86bb2c;
    --sun-orange: #f6b324;
    --ink-dark: #1c1c1c;
  }
  * { margin: 0; padding: 0; box-sizing: border-box; }
  html, body { width: 1200px; height: 1200px; overflow: hidden; }
  body {
    background: radial-gradient(circle at 50% 40%, #f7f7f7 0%, var(--page-bg) 75%);
    font-family: "Open Sans", Arial, sans-serif;
    position: relative;
  }
  .label {
    position: absolute;
    left: 280px; top: 220px;
    width: 640px; height: 760px;
    background: var(--label-black);
    border-radius: 18px;
    overflow: hidden;
  }
  .new-badge {
    position: absolute; left: 30px; top: 30px;
    width: 120px; height: 120px;
  }
  .new-badge span {
    position: absolute; inset: 0;
    display: flex; align-items: center; justify-content: center;
    color: #fff; font-weight: 800; font-size: 26px;
    transform: rotate(-20deg);
  }
  .brand {
    position: absolute; left: 100px; top: 110px;
    display: flex; align-items: center; gap: 18px;
  }
  .brand-name {
    font-family: "Questrial", Arial, sans-serif;
    font-size: 160px; line-height: 1;
    color: var(--brand-green);
    letter-spacing: -4px;
  }
  .brand-dot {
    width: 64px; height: 64px; border-radius: 50%;
    background: var(--sun-orange);
    margin-top: -70px;
  }
  .brand-by {
    position: absolute; left: 106px; top: 282px;
    color: var(--sun-orange);
    font-weight: 800; font-size: 22px;
  }
  .tagline-pill {
    position: absolute; left: 100px; top: 324px;
    width: 440px; height: 46px;
    background: var(--brand-green);
    border-radius: 8px;
    display: flex; align-items: center; justify-content: center;
    font-weight: 800; font-size: 22px; color: var(--ink-dark);
  }
  .intro-copy {
    position: absolute; left: 104px; top: 388px;
    width: 432px;
    color: var(--brand-green);
    font-size: 16px; line-height: 1.55;
    text-align: justify; text-align-last: center;
  }
  .wave-band { position: absolute; left: 0; top: 440px; width: 640px; height: 320px; }
  .benefit {
    position: absolute; left: 0; right: 0; top: 600px;
    text-align: center;
    color: var(--ink-dark);
    font-weight: 800; font-size: 26px; line-height: 1.4;
  }
  .net-weight {
    position: absolute; left: 0; right: 0; top: 690px;
    text-align: center; color: var(--ink-dark);
    font-size: 24px;
  }
</style>
</head>
<body>
  <main class="label">
    <svg class="wave-band" viewBox="0 0 640 320" aria-hidden="true">
      <path d="M0 40 C160 130 420 140 640 20 L640 320 L0 320 Z" fill="var(--wave-deep)"/>
      <path d="M0 70 C180 150 430 150 640 50 L640 320 L0 320 Z" fill="var(--brand-green)"/>
      <path d="M0 150 C200 110 420 210 640 150 L640 320 L0 320 Z" fill="var(--wave-light)" opacity="0.45"/>
    </svg>

    <div class="new-badge">
      <svg viewBox="0 0 120 120" width="120" height="120" aria-hidden="true">
        <g fill="var(--brand-green)">
          <rect x="22" y="22" width="76" height="76"/>
          <rect x="22" y="22" width="76" height="76" transform="rotate(22.5 60 60)"/>
          <rect x="22" y="22" width="76" height="76" transform="rotate(45 60 60)"/>
          <rect x="22" y="22" width="76" height="76" transform="rotate(67.5 60 60)"/>
        </g>
      </svg>
      <span>NEW</span>
    </div>

    <div class="brand">
      <span class="brand-name">Plume</span>
      <span class="brand-dot"></span>
    </div>
    <p class="brand-by">BY CORAVELLE</p>

    <p class="tagline-pill">THE SKIN MULTI-VITAMIN LOTION</p>

    <p class="intro-copy">Lorem ipsum dolor sit amet, consectetur adipisicing elit, sed do eiusmod tempor.</p>

    <p class="benefit">KEEPS SKIN SOFT,<br>SMOOTH AND SLIGHTLY MOIST</p>
    <p class="net-weight">Net Weight: 8oz</p>
  </main>
</body>
</html>
```